I challenge you to create Denmark's coolest roofing company website

We need to have a website created for our roofing company.

I have some pages that can be used as a starting point because there are some things we would like to have, one important thing is a roof calculator, in addition to that information about the company, pictures of tasks we have completed, links to Friendlio and Pictavoro pages.

reviews from rated, etc. should also be visible on the page.

we have lots of pictures, videos, logos,

we need to have a nice home page that is just a little cooler than the competitors.
we need to steal their customer. the page should be easy and clear but with a nice design.
an important thing is the calculator.
come up with some suggestions we are quite open as long as it is a nice design
Updates

I have made an update in the PDF file with some thoughts and wishes. The file has been uploaded.

Target Market(s)

20-60

Industry/Entity Type

carpenter - roofer

Coding

Coded - Design and coding required

Number of Pages Required

4 page

Font styles to use
Sans Serif

Colors
EB3D1F
EC4F4E
F09395
F8D3D4
FCEDEE

Requirements
Must have
• Roof calculator, nice design, easy to get around
Nice to have
• the competitors : https://mollerbyghuset.dk https://hvid-tegl.dk https://strandbyghuset.dk

```html
<!DOCTYPE html>
<html lang="en">
<head>
<meta charset="utf-8">
<title>Takværk – Roofing</title>
<link href="https://fonts.googleapis.com/css2?family=Red+Hat+Display:wght@400;500;600;700;800&display=swap" rel="stylesheet">
<style>
:root{
  --red:#EB3D1F;
  --red2:#EC4F4E;
  --rose:#F09395;
  --pink:#F8D3D4;
  --blush:#FCEDEE;
  --dark:#23272c;
  --ink:#1b1b1b;
  --grey:#555;
  --green:#00b67a;
  --line:#e4e4e4;
}
*{box-sizing:border-box;margin:0;padding:0}
html,body{width:1200px;height:4488px;overflow:hidden}
body{position:relative;font-family:"Red Hat Display",Arial,sans-serif;color:var(--ink);background:#fff}
.abs{position:absolute}
.btn{position:absolute;display:flex;align-items:center;justify-content:center;font-weight:700;font-size:12px;border-radius:2px}
.btn-red{background:var(--red);color:#fff}
.btn-outline{border:1.5px solid var(--red);color:var(--red);background:#fff;font-size:12px}
.ph{position:absolute}
.stars{color:var(--green);letter-spacing:2px}

/* header */
.site-header{position:absolute;left:0;top:0;width:1200px;height:62px;background:#fff}
.brand{position:absolute;display:flex;align-items:center;gap:8px;font-weight:800;color:var(--ink)}
.brand .dot{width:14px;height:14px;background:var(--red)}
.nav{position:absolute;left:484px;top:24px;display:flex;font-size:10.5px;font-weight:600}
.nav span{margin-right:38px}
.nav .phone{display:flex;align-items:center;gap:6px;margin-right:0}

/* hero */
.hero{left:0;top:62px;width:1200px;height:544px;background:linear-gradient(135deg,#3d4142 0%,#55595a 35%,#2e3a2c 70%,#1f2520 100%)}
.hero-rating{left:106px;top:244px;color:#fff;font-size:14px;font-weight:500;display:flex;gap:10px;align-items:center}
.hero-title{left:106px;top:272px;color:#fff;font-size:40px;font-weight:800;line-height:47px}
.quote-frame{left:793px;top:235px;width:300px;height:396px;border:1.5px solid var(--red)}
.quote-box{left:768px;top:218px;width:300px;height:388px;background:var(--red);color:#fff;text-align:center}
.quote-box h3{margin-top:28px;font-size:20px;font-weight:700}
.quote-box p{font-size:9px;margin-top:6px}
.field{position:absolute;left:25px;width:250px;height:29px;background:#fff;color:#555;font-size:9.5px;text-align:left;padding:9px 12px;border-radius:2px}

/* services */
.eyebrow{position:absolute;left:0;width:1200px;text-align:center;color:var(--red);font-size:14px;font-weight:600}
.section-title{position:absolute;left:0;width:1200px;text-align:center;font-size:29px;font-weight:700}
.card{position:absolute;top:801px;width:228px;height:314px;background:#fff;box-shadow:0 2px 10px rgba(0,0,0,.1)}
.card .img{position:absolute;left:0;top:0;width:228px;height:155px}
.card h4{position:absolute;left:18px;top:176px;color:var(--red);font-size:16px;font-weight:700}
.card p{position:absolute;left:18px;top:206px;width:195px;font-size:9.5px;line-height:15px;color:#444}
.card .more{position:absolute;left:18px;top:285px;font-size:9px;font-weight:700;color:var(--red)}
.card .bar{position:absolute;right:0;bottom:0;width:32px;height:3px;background:var(--ink)}

/* about */
.about-band{left:0;top:1284px;width:1200px;height:676px;background:var(--dark)}
.about-eyebrow{left:406px;top:1360px;color:var(--red);font-size:14px;font-weight:600}
.about-title{left:406px;top:1388px;width:600px;color:#fff;font-size:30px;font-weight:600;line-height:35px}
.about-text{left:406px;width:570px;color:#fff;font-size:9.5px;line-height:15px}

/* reviews */
.review{position:absolute;top:2247px;width:249px;height:195px;background:#fff;box-shadow:0 2px 10px rgba(0,0,0,.12);padding:16px}
.review .q{position:absolute;left:16px;top:18px;width:28px;height:28px;border-radius:50%;background:#eef3f0;color:var(--green);font-weight:800;font-size:18px;text-align:center;line-height:32px}
.review .name{position:absolute;left:62px;top:16px;font-size:11px;font-weight:700}
.review .date{position:absolute;left:62px;top:33px;font-size:8.5px;color:#aaa}
.review .stars{position:absolute;left:16px;top:60px;font-size:15px}
.review p{position:absolute;left:20px;top:94px;width:212px;font-size:8.8px;line-height:15px;color:#333}
.review p span{color:var(--red)}

/* calculator */
.calc{left:0;top:2578px;width:1200px;height:753px;background:linear-gradient(180deg,var(--blush) 0%,#f8e4e6 45%,#e8e7ee 68%,#d9dde6 100%)}
.calc-roof{left:0;top:3066px;width:1200px;height:265px;background:linear-gradient(170deg,rgba(0,0,0,0) 0%,rgba(0,0,0,0) 28%,#3c3f46 29%,#5a5e66 50%,#7c4a2a 51%,#c5561c 70%,#8d3a12 100%)}
.calc-frame{left:200px;top:2747px;width:800px;height:267px;border:1.5px solid var(--rose)}
.calc-title{left:0;top:2720px;width:1200px;text-align:center;font-size:40px;font-weight:700}
.calc-title span{color:var(--red)}
.step{position:absolute;top:2835px;width:28px;height:28px;border-radius:50%;font-size:10px;font-weight:700;display:flex;align-items:center;justify-content:center}
.pill{position:absolute;top:2946px;height:22px;border:1.5px solid #333;border-radius:12px;font-size:10px;font-weight:600;display:flex;align-items:center;justify-content:center;background:#fff}

/* gallery */
.gal{position:absolute}

/* footer */
.footer{left:0;top:4163px;width:1200px;height:325px;background:var(--blush)}
.f-title{position:absolute;font-size:15px;font-weight:700}
.f-text{position:absolute;font-size:10px;line-height:16px;color:#222}
.social{position:absolute;top:4434px;width:30px;height:30px;border-radius:50%;border:1.5px solid var(--red)}
</style>
</head>
<body>

<header class="site-header">
  <div class="brand" style="left:125px;top:16px;font-size:22px;"><span class="dot"></span>Takværk</div>
  <nav class="nav">
    <span>Home</span><span>About</span><span>Services</span><span>Gallery</span><span>Review</span><span>Contact Us</span>
    <span class="phone"><svg width="11" height="11" viewBox="0 0 24 24"><path fill="#EB3D1F" d="M6.6 10.8a15 15 0 006.6 6.6l2.2-2.2c.3-.3.7-.4 1-.2 1.1.4 2.3.6 3.6.6.6 0 1 .4 1 1V20c0 .6-.4 1-1 1A17 17 0 013 4c0-.6.4-1 1-1h3.5c.6 0 1 .4 1 1 0 1.3.2 2.5.6 3.6.1.3 0 .7-.2 1z"/></svg>40 12 57 63</span>
  </nav>
  <div class="btn btn-red" style="left:990px;top:16px;width:104px;height:31px;">Get a Quote</div>
</header>

<section class="abs hero" role="img" aria-label="Aerial photo of a house with a dark grey tiled roof surrounded by trees"></section>
<div class="abs hero-rating">4.2 out of 5 <span class="stars">★★★★★</span> Ratedly &amp; Searchly</div>
<h1 class="abs hero-title">We Make Your Roofing<br>Dreams Come True.</h1>
<div class="btn btn-red" style="left:106px;top:395px;width:138px;height:29px;">Contact Us Today!</div>

<div class="abs quote-frame"></div>
<form class="abs quote-box">
  <h3>Get A Quote</h3>
  <p>Fill in the form below and we'll call you.</p>
  <div class="field" style="top:95px;">Name</div>
  <div class="field" style="top:139px;">Phone</div>
  <div class="field" style="top:182px;">Email...</div>
  <div class="field" style="top:226px;">Address...</div>
  <div class="field" style="top:270px;height:43px;padding-top:16px;">How can we help you?</div>
  <div class="btn" style="left:99px;top:327px;width:104px;height:30px;background:#111;color:#fff;font-size:11px;">Get a Quote</div>
</form>

<div class="eyebrow" style="top:706px;">What we do</div>
<h2 class="section-title" style="top:736px;">We Can Help You With...</h2>

<article class="card" style="left:106px;">
  <div class="img" role="img" aria-label="Photo of a new house with a dark slate roof" style="background:linear-gradient(180deg,#8fb0d6,#4a5662 60%,#2f3a44)"></div>
  <h4>New Roof</h4>
  <p>There are many variations of work passages of Lorem Ipsum available, but the majority have suffered alteration in some form, by injected...</p>
  <div class="more">Read More ↗</div><div class="bar"></div>
</article>
<article class="card" style="left:359px;">
  <div class="img" role="img" aria-label="Photo of a roofer working on a metal roof" style="background:linear-gradient(180deg,#9cc0e4,#4f6a8c 45%,#2e3c55)"></div>
  <h4>Roof Renovation</h4>
  <p>There are many variations of work passages of Lorem Ipsum available, but the majority have suffered alteration in some form, by injected...</p>
  <div class="more">Read More ↗</div><div class="bar"></div>
</article>
<article class="card" style="left:613px;">
  <div class="img" role="img" aria-label="Photo of a damaged roof with a ladder" style="background:linear-gradient(180deg,#c9d9ea,#3f5472 40%,#22324a)"></div>
  <h4>Acute Damage</h4>
  <p>There are many variations of work passages of Lorem Ipsum available, but the majority have suffered alteration in some form, by injected...</p>
  <div class="more">Read More ↗</div><div class="bar"></div>
</article>
<article class="card" style="left:866px;">
  <div class="img" role="img" aria-label="Photo of a carpenter working with wood in a workshop" style="background:linear-gradient(135deg,#d8c3a8,#9a7b5c 55%,#5a4433)"></div>
  <h4>Carpenter</h4>
  <p>There are many variations of work passages of Lorem Ipsum available, but the majority have suffered alteration in some form, by injected...</p>
  <div class="more">Read More ↗</div><div class="bar"></div>
</article>
<div class="btn btn-outline" style="left:545px;top:1146px;width:110px;height:32px;">Explore More</div>

<section class="abs about-band"></section>
<div class="ph" role="img" aria-label="Photo of a house with dark wooden cladding and a slate roof" style="left:0;top:1253px;width:343px;height:344px;background:linear-gradient(180deg,#6aa6e6 0%,#9cc5ea 35%,#3e4448 55%,#4a7a3a 85%,#5c8a3c)"></div>
<div class="abs about-eyebrow">Takværk</div>
<h2 class="abs about-title">Specialists in new roofs, roofing work and roof renovations</h2>
<p class="abs about-text" style="top:1478px;">Lorem Ipsum is simply dummy text of the printing and typesetting industry. Lorem Ipsum has been the industry's standard dummy text ever since the 1500s, when an unknown printer took a galley of type and scrambled it to make a type specimen book.</p>
<p class="abs about-text" style="top:1536px;">It has survived not only five centuries, but also the leap into electronic typesetting, remaining essentially unchanged. It was popularised in the 1960s with the release of printed sheets containing Lorem Ipsum passages, and more recently with desktop publishing software including many versions of Lorem Ipsum...</p>
<div class="btn btn-red" style="left:406px;top:1611px;width:115px;height:30px;">Discover More</div>
<div class="ph" role="img" aria-label="Photo of a standing seam metal roof on a white house against blue sky" style="left:406px;top:1691px;width:794px;height:344px;background:linear-gradient(160deg,#3d7fd4 0%,#5b8e3c 28%,#4b4e5c 42%,#3a3d49 65%,#e9e6df 80%,#f4f2ec)"></div>

<div class="abs" style="left:0;top:2118px;width:1200px;display:flex;justify-content:center;align-items:center;gap:7px;font-size:15px;font-weight:600;">
  <span style="width:10px;height:10px;background:var(--green);display:block"></span>Ratedly
</div>
<h2 class="section-title" style="top:2152px;">We Love Happy Customers</h2>
<div class="abs" style="left:0;top:2200px;width:1200px;text-align:center;font-size:10px;"><b>Excellent:</b> <span class="stars" style="font-size:13px;">★★★★★</span> 4.2 out of 5 42 reviews - ratedly and searchly</div>

<article class="review" style="left:202px;">
  <div class="q">❞</div><div class="name">Maja K</div><div class="date">July 11, 2025</div>
  <div class="stars">★★★★★</div>
  <p>It is a long established fact that a reader will be distracted by the readable content of a page when looking at its layout. the point of using lorem ipsum is that it has a more-or-less normal distribution... <span>[more]</span></p>
</article>
<article class="review" style="left:477px;">
  <div class="q">❞</div><div class="name">Lars Holm</div><div class="date">June 18, 2025</div>
  <div class="stars">★★★★★</div>
  <p>It is a long established fact that a reader will be distracted by the readable content of a page when looking at its layout. the point of using lorem ipsum is that it has a more-or-less normal distribution... <span>[more]</span></p>
</article>
<article class="review" style="left:752px;">
  <div class="q">❞</div><div class="name">Sofie Brandt</div><div class="date">February 16, 2025</div>
  <div class="stars">★★★★★</div>
  <p>It is a long established fact that a reader will be distracted by the readable content of a page when looking at its layout. the point of using lorem ipsum is that it has a more-or-less normal distribution... <span>[more]</span></p>
</article>
<div class="btn btn-outline" style="left:545px;top:2472px;width:110px;height:31px;">Explore More</div>

<section class="abs calc"></section>
<div class="ph calc-roof" role="img" aria-label="Photo of a modern house with orange wooden cladding and a metal roof"></div>
<div class="abs calc-frame"></div>
<h2 class="abs calc-title"><span style="color:var(--ink);background:#fbebed;padding:0 10px;">Roof <span>Calculator</span></span></h2>
<p class="abs" style="left:0;top:2786px;width:1200px;text-align:center;font-size:14px;">Enter your details below and we'll calculate your conveyancing fees in 30 seconds.</p>
<svg class="abs" style="left:436px;top:2848px;" width="330" height="2"><line x1="0" y1="1" x2="330" y2="1" stroke="#F09395" stroke-width="1.5"/></svg>
<div class="step" style="left:408px;background:var(--red);color:#fff;">1</div>
<div class="step" style="left:585px;background:#fff;border:1.5px solid var(--rose);">2</div>
<div class="step" style="left:763px;background:#fff;border:1.5px solid var(--rose);">3</div>
<svg class="abs" style="left:311px;top:2904px;" width="578" height="2"><line x1="0" y1="1" x2="108" y2="1" stroke="#333"/><line x1="470" y1="1" x2="578" y2="1" stroke="#333"/></svg>
<div class="abs" style="left:0;top:2894px;width:1200px;text-align:center;font-size:17px;font-weight:700;">Select A Roof Yours Most Resembles</div>
<div class="pill" style="left:275px;width:108px;">Cross Hipped</div>
<div class="pill" style="left:390px;width:75px;background:var(--red);border-color:var(--red);color:#fff;">Dormer</div>
<div class="pill" style="left:473px;width:53px;">Hip</div>
<div class="pill" style="left:533px;width:107px;">Hip &amp; Valley</div>
<div class="pill" style="left:642px;width:170px;">Intersecting / Overlaid Hip</div>
<div class="pill" style="left:822px;width:103px;">Open Gable</div>
<div class="btn" style="left:524px;top:3002px;width:150px;height:29px;background:var(--pink);color:#333;font-size:11px;">Get A&nbsp;<i>FREE</i>&nbsp;Estimate</div>

<div class="eyebrow" style="top:3405px;">Gallery</div>
<h2 class="section-title" style="top:3435px;">We Have Completed Work</h2>
<div class="gal" role="img" aria-label="Photo of a white rendered house with a dark tiled roof and flagpole" style="left:105px;top:3543px;width:313px;height:438px;background:linear-gradient(180deg,#3f7fd6 0%,#8db4e8 28%,#3a3c40 45%,#cfcabc 62%,#5f9a3a 85%)"></div>
<div class="gal" role="img" aria-label="Photo of a house with a new orange tiled roof" style="left:442px;top:3500px;width:314px;height:249px;background:linear-gradient(180deg,#3d7bd3 0%,#c8683a 35%,#d9743f 55%,#2c3034 80%)"></div>
<div class="gal" role="img" aria-label="Photo of a zinc clad dormer on a slate roof" style="left:442px;top:3773px;width:314px;height:251px;background:linear-gradient(135deg,#a9c4df 0%,#6d8195 40%,#4c5a66 70%,#2f3840)"></div>
<div class="gal" role="img" aria-label="Photo of an orange tiled roof with a white dormer" style="left:782px;top:3543px;width:314px;height:438px;background:linear-gradient(160deg,#6aa0e0 0%,#b85a2e 25%,#c96a38 55%,#8a3a18 100%)"></div>
<div class="btn btn-outline" style="left:543px;top:4057px;width:112px;height:30px;">View All Work</div>

<footer class="abs footer"></footer>
<div class="brand" style="left:200px;top:4248px;font-size:30px;"><span class="dot" style="width:18px;height:18px;"></span>Takværk</div>
<p class="f-text" style="left:200px;top:4320px;width:240px;">We always deliver high quality workmanship, good service and effective solutions at competitive prices.</p>

<div class="f-title" style="left:512px;top:4235px;">Contact us</div>
<div class="f-text" style="left:512px;top:4266px;font-size:12px;display:flex;gap:6px;align-items:center;"><span style="color:var(--red)">☏</span>40 12 57 63</div>
<div class="f-text" style="left:512px;top:4292px;display:flex;gap:6px;"><span style="color:var(--red)">✉</span>info@takvaerk.dk</div>
<div class="f-text" style="left:512px;top:4318px;display:flex;gap:6px;"><svg width="9" height="12" viewBox="0 0 9 12" style="margin-top:2px"><path fill="#EB3D1F" d="M4.5 0A4.5 4.5 0 000 4.5C0 8 4.5 12 4.5 12S9 8 9 4.5A4.5 4.5 0 004.5 0zm0 6.2a1.7 1.7 0 110-3.4 1.7 1.7 0 010 3.4z"/></svg><span>Takværk ApS Skovbrynet 12,<br>4000 Roskilde</span></div>
<div class="f-text" style="left:512px;top:4366px;color:var(--red);text-decoration:underline;">Get Directions ↗</div>

<div class="f-title" style="left:793px;top:4235px;">Quick links</div>
<div class="f-text" style="left:793px;top:4266px;line-height:26px;"><span style="color:var(--red)">Home</span><br>About us<br>Services<br>Gallery<br>Reviews</div>
<div class="f-text" style="left:873px;top:4266px;line-height:26px;">Contact Us<br>Terms and conditions<br>Privacy policy</div>
<svg class="abs" style="left:1084px;top:4412px;" width="20" height="20" viewBox="0 0 20 20"><path d="M10 2L17 18 10 14 3 18z" fill="#EB3D1F"/></svg>

<div class="abs" style="left:200px;top:4428px;width:900px;height:1px;background:#e6c9cb;"></div>
<div class="f-text" style="left:200px;top:4444px;font-size:9px;">© 2025 <span style="color:var(--red)">Takværk</span>. All Rights Reserved</div>
<div class="f-text" style="left:512px;top:4444px;font-size:9px;"><b>Monday – Friday:</b> 8:00 AM – 4:00 PM</div>
<a class="social" style="left:793px;" aria-label="Pictavoro"></a>
<a class="social" style="left:832px;" aria-label="Friendlio"></a>

</body>
</html>
```